Looking to design a new sign for our church.

Looking for a new sign
4 x 8 feet dimension
We are renaming the church "Medlow Ridge Community Church"
looking for legible graphics
Would like some type of backdrop being a family tree (oak) / open to other ideas as you are led
I have included a pic of the old sign for your review
would like to incorporate our Kindred Ministries on the lower right hand corner of the sign / see file attached

```html
<!DOCTYPE html>
<html lang="en">
<head>
<meta charset="utf-8">
<title>Medlow Ridge Community Church – Sign</title>
<link rel="stylesheet" href="https://fonts.googleapis.com/css2?family=Lato:wght@400;700;900&display=swap">
<style>
  :root {
    --backdrop: #ecebe8;
    --sign-white: #ffffff;
    --frame: #1f1f1f;
    --band-brown: #4a3a2e;
    --ink: #1c1c1c;
    --tree-tone: #c9864a;
    --tree-tone-deep: #5a4536;
    --band-text: #f4efe9;
  }
  * { box-sizing: border-box; margin: 0; padding: 0; }
  html, body {
    width: 900px;
    height: 1200px;
    overflow: hidden;
    background: var(--backdrop);
    font-family: "Lato", Arial, sans-serif;
  }
  .canvas {
    position: relative;
    width: 900px;
    height: 1200px;
  }
  .sign {
    position: absolute;
    left: 30px;
    top: 376px;
    width: 840px;
    height: 448px;
    background: var(--sign-white);
    border: 4px solid var(--frame);
    display: flex;
    box-shadow: 0 10px 30px rgba(0,0,0,0.12);
  }
  .sign-main {
    flex: 1;
    display: flex;
    align-items: center;
    padding: 0 30px 0 40px;
  }
  .tree-emblem {
    width: 175px;
    height: 175px;
    border-radius: 50%;
    background: radial-gradient(circle at 50% 40%, var(--tree-tone) 0%, #b5703a 55%, var(--tree-tone-deep) 100%);
    flex-shrink: 0;
    margin-right: 36px;
  }
  .church-name {
    color: var(--ink);
    line-height: 1.05;
  }
  .church-name .name-line {
    display: block;
    font-weight: 900;
    font-size: 42px;
    letter-spacing: 0.2px;
    text-transform: uppercase;
  }
  .church-name .sub-line {
    display: block;
    font-weight: 700;
    font-size: 30px;
    text-transform: uppercase;
    margin-top: 6px;
  }
  .service-times {
    list-style: none;
    margin-top: 20px;
    color: var(--ink);
    font-size: 17px;
    line-height: 1.35;
  }
  .service-times li:last-child { font-weight: 700; }
  .ministry-band {
    width: 186px;
    background: var(--band-brown);
    display: flex;
    flex-direction: column;
    align-items: center;
    justify-content: center;
    gap: 14px;
  }
  .ministry-mark {
    width: 38px;
    height: 38px;
    border-radius: 50%;
    background: var(--band-text);
  }
  .ministry-name {
    color: var(--band-text);
    font-weight: 700;
    font-size: 17px;
    text-align: center;
    line-height: 1.25;
  }
</style>
</head>
<body>
  <main class="canvas">
    <section class="sign" aria-label="Church sign">
      <div class="sign-main">
        <div class="tree-emblem" role="img" aria-label="Oak family tree emblem with autumn leaves"></div>
        <div class="church-info">
          <h1 class="church-name">
            <span class="name-line">Medlow Ridge</span>
            <span class="sub-line">Community Church</span>
          </h1>
          <ul class="service-times">
            <li>10:30am Worship Service</li>
            <li>9:30am Sunday School</li>
            <li>6:00pm Wednesday Service</li>
          </ul>
        </div>
      </div>
      <aside class="ministry-band">
        <span class="ministry-mark" aria-hidden="true"></span>
        <span class="ministry-name">Kindred<br>Ministries</span>
      </aside>
    </section>
  </main>
</body>
</html>
```